New Business Card Design for Manufacturing

We are an engineering/manufacturing company that offers Advanced machining/assembly/engineering services, as well as innovative products for the heavy duty engine cooling markets.

We are looking to get a new business card designed that is clean and modern looking, but still fits the wide range of technical/skilled work we do.

- We hope to use this design as the base for other design work in new Presentations, web, and print work.

Industry/Entity Type

Engineering

Contact Information for Business Card

Our preferred color of blue is (RGB) 22/71/159 but can vary slightly from that color. Our content will be our Logo and full company name (Fabricated Tooling Works, Inc.), company address, name, job title, phone number with extension, cell number, fax number, website, and email address on the cards.
We'd like the full company name next to the logo, but we are open to other interpretations of that layout.
Preferably, we would like the back side to be clean with just our logo, and the front to contain all of the contact information.

Colors
2f74b4
0355a3
85abd2

Requirements
Must have
• - Logo, company name, needed content - We are open to interpretation beyond that.
• - Standard size business card.
• - Horizontal orientation.
• - Enough space for lengthy names / job titles (for example, a job title could read "Directory of Human Resources" or "V.P. of Governmental Affairs"). We need this to look clean, whether the title be short (CEO) or long (as described above).

```html
<!DOCTYPE html>
<html lang="en">
<head>
<meta charset="utf-8">
<title>Fabricated Tooling Works, Inc. — Business Card</title>
<link rel="stylesheet" href="https://fonts.googleapis.com/css2?family=Arimo:wght@400;700&display=swap">
<style>
  :root {
    --backdrop: #a3a3a3;
    --card-white: #ffffff;
    --brand-blue: #1151a0;
    --steel-gray: #7d838a;
    --tagline-gray: #8a8d91;
    --text-dark: #2b2b2b;
    --rule-gray: #9a9a9a;
  }
  * { margin: 0; padding: 0; box-sizing: border-box; }
  html, body { width: 1200px; height: 900px; overflow: hidden; }
  body {
    background: var(--backdrop);
    font-family: "Arimo", Arial, sans-serif;
    position: relative;
  }
  .card {
    position: absolute;
    top: 286px;
    width: 530px;
    height: 328px;
    overflow: hidden;
  }
  .card-front { left: 58px; background: var(--card-white); }
  .card-back { left: 612px; background: var(--steel-gray); }

  .brand { position: absolute; left: 34px; top: 112px; width: 226px; }
  .brand-name {
    display: block;
    font-weight: 700;
    font-size: 78px;
    line-height: 1;
    letter-spacing: 2px;
    color: var(--brand-blue);
  }
  .brand-company {
    display: block;
    margin-top: 8px;
    font-weight: 700;
    font-size: 12px;
    letter-spacing: 0.2px;
    color: var(--tagline-gray);
    text-transform: uppercase;
    white-space: nowrap;
  }

  .contact { position: absolute; left: 272px; width: 236px; top: 58px; text-align: center; }
  .person-name {
    font-weight: 700;
    font-size: 20px;
    color: var(--brand-blue);
    letter-spacing: 0.3px;
    line-height: 24px;
  }
  .person-title { font-size: 16px; color: var(--text-dark); line-height: 20px; }
  .rule { width: 166px; height: 1px; background: var(--rule-gray); margin: 10px auto 12px; }
  .contact-list { list-style: none; }
  .contact-list li { font-size: 16px; line-height: 20px; color: var(--text-dark); }
  .contact-label { font-weight: 700; color: var(--brand-blue); }
  .address { font-size: 16px; line-height: 20.5px; color: var(--text-dark); font-style: normal; }

  .back-field { position: absolute; left: 0; top: 0; width: 100%; height: 180px; background: var(--brand-blue); }
  .back-band {
    position: absolute;
    left: 0; right: 0; top: 144px;
    height: 72px;
    background: var(--card-white);
    text-align: center;
  }
  .back-brand {
    font-weight: 700;
    font-size: 64px;
    line-height: 72px;
    letter-spacing: 3px;
    color: var(--brand-blue);
  }
  .website {
    position: absolute;
    left: 0; right: 0; top: 270px;
    text-align: center;
    font-weight: 700;
    font-size: 16px;
    letter-spacing: 1.6px;
    color: var(--card-white);
  }
</style>
</head>
<body>
  <section class="card card-front">
    <div class="brand">
      <span class="brand-name">FTW</span>
      <span class="brand-company">Fabricated Tooling Works, Inc.</span>
    </div>
    <div class="contact">
      <p class="person-name">DANIEL HARTLEY</p>
      <p class="person-title">Managing Director</p>
      <div class="rule"></div>
      <ul class="contact-list">
        <li><span class="contact-label">P:</span> (044)123456789</li>
        <li><span class="contact-label">M:</span> (044)123456789</li>
        <li><span class="contact-label">F:</span> (044)123456789</li>
        <li><span class="contact-label">E:</span> info@youremail.com</li>
      </ul>
      <div class="rule"></div>
      <address class="address">1234, Address GoesHere,<br>Country name, 12345</address>
    </div>
  </section>

  <section class="card card-back">
    <div class="back-field"></div>
    <div class="back-band">
      <p class="back-brand">FTW</p>
    </div>
    <p class="website">WWW.WEBSITENAME.COM</p>
  </section>
</body>
</html>
```